Corvale Spine & Joint Business Card

Need a business card using the logo provided. I want brand side of the card to be grey with the logo in the center of the card in white.

On the other side I leave to the designers

Target Market(s)

Personal Injury Attorneys

Industry/Entity Type

Medical

Contact Information for Business Card

Name, CEO. Cell Phone, (Hialeah, Address, Phone) (Homestead, Address, Phone) (Tallahassee, Address, Phone)

Colors

Designer to choose only greyscale colors for use in the design.

Requirements
Must have
• Logo by itself on one side

```html
<!DOCTYPE html>
<html lang="en">
<head>
<meta charset="utf-8">
<title>Corvale Spine &amp; Joint — Business Card</title>
<link href="https://fonts.googleapis.com/css2?family=Open+Sans:wght@400;700&display=swap" rel="stylesheet">
<style>
  :root {
    --backdrop: #cbc9ca;
    --card: #a9adb0;
    --ink-dark: #4b4f54;
    --white: #ffffff;
  }
  * { margin: 0; padding: 0; box-sizing: border-box; }
  html, body {
    width: 1200px; height: 1200px; overflow: hidden;
    background: var(--backdrop);
    font-family: "Open Sans", sans-serif;
  }
  .canvas { position: relative; width: 1200px; height: 1200px; }
  .card {
    position: absolute; left: 229px; width: 745px;
    background: var(--card);
  }
  .card--info { top: 163px; height: 419px; }
  .card--brand { top: 620px; height: 414px; }

  .brand-name {
    position: absolute;
    font-weight: 700; text-transform: uppercase; line-height: 1;
    white-space: nowrap;
  }
  .card--info .brand-name {
    left: 27px; top: 60px;
    font-size: 34px; letter-spacing: 3px; color: var(--ink-dark);
  }
  .card--brand .brand-name {
    left: 0; right: 0; top: 187px; text-align: center;
    font-size: 40px; letter-spacing: 4px; color: var(--white);
  }

  .holder { position: absolute; left: 27px; top: 250px; }
  .holder__name { font-weight: 700; font-size: 29px; color: var(--ink-dark); line-height: 1.1; }
  .holder__title { font-weight: 400; font-size: 18px; color: var(--white); margin-top: 6px; }

  .divider {
    position: absolute; left: 27px; top: 323px; width: 690px; height: 1.5px;
    background: var(--ink-dark);
  }

  .phones {
    position: absolute; left: 27px; top: 344px; list-style: none;
    font-size: 18px; color: var(--white);
  }
  .phones li { display: flex; align-items: center; height: 29px; }
  .phones svg { width: 16px; height: 18px; margin-right: 4px; }

  .address {
    position: absolute; right: 28px; top: 340px; text-align: right;
    font-size: 18px; color: var(--white);
    font-style: normal; line-height: 29px;
  }
</style>
</head>
<body>
<main class="canvas">
  <section class="card card--info">
    <p class="brand-name">Corvale Spine &amp; Joint</p>
    <div class="holder">
      <p class="holder__name">DANE HOLLOWAY</p>
      <p class="holder__title">CEO</p>
    </div>
    <div class="divider"></div>
    <ul class="phones">
      <li>
        <svg viewBox="0 0 16 18" aria-hidden="true"><rect x="3" y="1" width="10" height="16" rx="1.5" fill="none" stroke="#4b4f54" stroke-width="1.6"/><circle cx="8" cy="14.5" r="0.9" fill="#4b4f54"/></svg>
        +123-456-789
      </li>
      <li>
        <svg viewBox="0 0 16 18" aria-hidden="true"><path d="M3 3.5c1-1 2-1 2.6 0l1.2 2c.4.7.2 1.3-.4 1.8l-.8.6c.6 1.6 1.9 2.9 3.5 3.6l.6-.8c.5-.6 1.1-.8 1.8-.4l2 1.2c1 .6 1 1.6 0 2.6-1.2 1.2-3 1.4-5 .2C5.5 12.6 3.7 10.8 2.6 8.8 1.5 6.6 1.8 4.7 3 3.5z" fill="#4b4f54"/><path d="M10 2.5a4.5 4.5 0 0 1 4 4M10 4.8a2.3 2.3 0 0 1 1.8 1.8" fill="none" stroke="#4b4f54" stroke-width="1.2" stroke-linecap="round"/></svg>
        +123-456-789
      </li>
    </ul>
    <address class="address">
      4120 Harborline Avenue #215<br>
      Westbrook, CA 90344
    </address>
  </section>

  <section class="card card--brand">
    <p class="brand-name">Corvale Spine &amp; Joint</p>
  </section>
</main>
</body>
</html>
```